Corvel Lane

Small ageny public transit advocacy, funding and compliance.
Consulting and lobbying efforts for small public transit agencies and communities exploring public transit opportunities.
Updates

I was interested in a simple line sketch suggesting motion, mobility. The card will be black on white. I would like it to include the bUs ones brief; Advocacy, Funding , and Compliance for small transit agencies.

Reason: I have been traveling and have had limited time to respond. Thank you all for your submit talks.

Industry/Entity Type

Consulting

Contact Information for Business Card

Mark D Loyer
Phone (614) 380-2917
Email markdloyer@vantomail.test

```html
<!DOCTYPE html>
<html lang="en">
<head>
<meta charset="utf-8">
<title>Corvel Lane – Business Card</title>
<link rel="stylesheet" href="https://fonts.googleapis.com/css2?family=Cabin:wght@400;700&display=swap">
<style>
  :root {
    --card-black: #000000;
    --ink-white: #ffffff;
    --emblem-light: #ffffff;
    --emblem-soft: #e6e6e6;
  }
  html, body {
    margin: 0;
    padding: 0;
    width: 762px;
    height: 1200px;
    overflow: hidden;
    background: var(--card-black);
  }
  .card {
    position: relative;
    width: 762px;
    height: 1200px;
    background: var(--card-black);
    color: var(--ink-white);
    font-family: "Cabin", "Gill Sans", sans-serif;
  }
  .services {
    position: absolute;
    top: 50px;
    left: 0;
    width: 762px;
    margin: 0;
    text-align: center;
    font-weight: 700;
    font-size: 54px;
    line-height: 56px;
    letter-spacing: 0;
  }
  .emblem-area {
    position: absolute;
    top: 241px;
    left: 230px;
    width: 303px;
    height: 423px;
    background: linear-gradient(180deg, var(--emblem-light), var(--emblem-soft));
  }
  .brand-name {
    position: absolute;
    top: 700px;
    left: 0;
    width: 762px;
    margin: 0;
    text-align: center;
    font-weight: 700;
    font-size: 44px;
    line-height: 52px;
  }
  .brand-focus {
    position: absolute;
    top: 762px;
    left: 0;
    width: 762px;
    margin: 0;
    text-align: center;
    font-weight: 400;
    font-size: 24px;
    line-height: 32px;
  }
  .contact {
    position: absolute;
    left: 0;
    width: 762px;
    margin: 0;
    text-align: center;
    font-weight: 400;
    letter-spacing: -1px;
    line-height: 1;
  }
  .contact-name { top: 938px; font-size: 44px; }
  .contact-phone {
    top: 1012px;
    font-size: 44px;
    display: flex;
    justify-content: center;
    align-items: center;
    gap: 8px;
    padding-right: 40px;
    box-sizing: border-box;
  }
  .phone-icon { width: 42px; height: 34px; }
  .phone-icon rect { fill: var(--ink-white); }
  .contact-email { top: 1094px; font-size: 48px; }
</style>
</head>
<body>
  <main class="card">
    <h1 class="services">Consulting<br>and<br>lobbying</h1>

    <div class="emblem-area" role="img" aria-label="Simple line sketch suggesting transit motion and mobility"></div>

    <p class="brand-name">Corvel Lane</p>
    <p class="brand-focus">Advocacy, Funding and Compliance for small transit agencies</p>

    <p class="contact contact-name">Mark D Loyer</p>
    <p class="contact contact-phone">
      <svg class="phone-icon" viewBox="0 0 40 32" aria-label="Phone">
        <rect x="0" y="6" width="8" height="5"/><rect x="0" y="14" width="8" height="5"/><rect x="0" y="22" width="8" height="5"/>
        <rect x="11" y="6" width="8" height="5"/><rect x="11" y="14" width="8" height="5"/><rect x="11" y="22" width="8" height="5"/>
        <rect x="22" y="0" width="8" height="5"/><rect x="22" y="6" width="8" height="5"/><rect x="22" y="14" width="8" height="5"/><rect x="22" y="22" width="8" height="5"/>
        <rect x="32" y="0" width="8" height="27"/>
      </svg>
      <span>(614) 380-2917</span>
    </p>
    <p class="contact contact-email">markdloyer@vantomail.test</p>
  </main>
</body>
</html>
```